Course flyer - evolutive design

We want to have a nice design for our course programm.
In fact we are school language, and our course programm change approximatively each 2 weeks§.
For that we need a design that we can modify each 2 weeks (only dates change ) by ourselves.
We used to have a classical design but we want to upgrade it with a modern and attractive design.
We can have 3 versions one for each city.
We have 3 offices: Tunis, Sousse & Sfax
Attached you can find old designs

Target Market(s)

students from 16 years old till retired people 76 years old

Industry/Entity Type

Education

Font styles to use
Sans Serif

Requirements
Must have
• clear timing for courses (date, days, timing)
• prices
• Adresse (each flyer has its own adress)
• phone Number
• Cool image
Should not have
• Racism
• Violence
• Too much stuff

```html
<!DOCTYPE html>
<html lang="fr">
<head>
<meta charset="utf-8">
<title>Cours d'allemand – Avril | Mai 2016</title>
<link href="https://fonts.googleapis.com/css2?family=Oswald:wght@300;400;700&family=Open+Sans:ital,wght@0,400;0,600;0,700;0,800;1,400&display=swap" rel="stylesheet">
<style>
  :root {
    --brown: #6b5751;
    --brown-soft: #9c8c82;
    --cream: #f0ecc6;
    --cream-light: #f7f5de;
    --yellow: #f8f0a2;
    --lime: #cdd62c;
    --ink: #151515;
    --white: #ffffff;
  }
  * { box-sizing: border-box; margin: 0; padding: 0; }
  html, body { width: 900px; height: 1200px; overflow: hidden; background: #ffffff; }
  body { font-family: "Open Sans", Arial, sans-serif; color: var(--brown); }

  .flyer { position: relative; width: 900px; height: 1200px; background: var(--white); overflow: hidden; }

  /* left column */
  .brand { position: absolute; left: 0; top: 0; width: 387px; height: 402px; display: flex; align-items: center; justify-content: center; gap: 14px; }
  .brand-dot { width: 34px; height: 34px; border-radius: 50%; background: var(--brown); }
  .brand-name { font-weight: 700; font-size: 44px; color: var(--brown); letter-spacing: -1px; }

  .rule-lime { position: absolute; height: 4px; background: var(--lime); }
  .rule-lime.top { left: 0; top: 402px; width: 387px; }
  .rule-lime.bottom { left: 0; top: 872px; width: 900px; }

  .photo-class { position: absolute; left: 0; top: 408px; width: 387px; height: 242px;
    background: linear-gradient(120deg, #c9a48c 0%, #e8d8c8 40%, #f2ede4 70%, #b8c9a8 100%); }

  .address { position: absolute; left: 0; top: 650px; width: 387px; height: 222px; text-align: center; padding-top: 20px; }
  .address h2 { font-weight: 400; font-size: 27px; letter-spacing: 1px; margin-bottom: 4px; }
  .address p { font-size: 15px; line-height: 19px; }
  .contact { margin-top: 8px; display: flex; flex-direction: column; align-items: center; gap: 2px; }
  .contact-line { display: flex; align-items: center; gap: 6px; font-size: 15px; }
  .contact-line.phone { font-weight: 700; font-size: 18px; }
  .contact-line svg { width: 11px; height: 11px; }

  .divider { position: absolute; left: 387px; top: 0; width: 6px; height: 872px; background: var(--brown); }

  /* right column */
  .schedule { position: absolute; left: 393px; top: 0; width: 507px; height: 872px; background: var(--cream); }
  .schedule-head { height: 130px; background: var(--brown); display: flex; align-items: center; justify-content: center; }
  .schedule-head h1 { font-family: "Oswald", "Arial Narrow", sans-serif; font-weight: 700; font-size: 52px; color: var(--yellow); letter-spacing: 2px; }
  .period { position: relative; margin-top: 8px; height: 54px; border-top: 2px solid var(--brown-soft); border-bottom: 2px solid var(--brown-soft);
    display: flex; align-items: center; padding-left: 34px; font-weight: 800; font-size: 32px; color: var(--ink); }
  .period .sep { display: inline-block; width: 3px; height: 26px; background: var(--ink); margin: 0 12px; }
  .period .year { position: absolute; right: 52px; font-size: 38px; }

  .session { position: absolute; left: 21px; width: 446px; border: 2px solid var(--brown-soft); border-radius: 10px; overflow: hidden; background: var(--cream-light); }
  .session-title { background: var(--brown-soft); color: var(--white); text-align: center; font-weight: 700; font-size: 15px; line-height: 19px; padding: 7px 0 8px; }
  .session-grid { display: grid; grid-template-columns: 1fr 1fr; position: relative; }
  .session-grid::after { content: ""; position: absolute; left: 50%; top: 0; bottom: 0; width: 3px; margin-left: -1px; background: var(--brown-soft); }
  .slot { background: var(--brown-soft); color: var(--white); font-size: 15px; height: 28px; line-height: 28px; margin-top: 6px; }
  .slot.left { padding-left: 30px; }
  .slot.center { text-align: center; }
  .groups { padding: 10px 0 12px; font-size: 15px; line-height: 17.5px; color: var(--ink); }
  .groups.left { padding-left: 30px; }
  .groups.center { padding-left: 62px; }
  .session .groups.mid { padding-left: 60px; }

  .s1 { top: 214px; min-height: 166px; }
  .s2 { top: 404px; min-height: 200px; }
  .s3 { top: 626px; min-height: 220px; }
  .s2 .groups.right, .s3 .groups.right { padding-top: 14px; }

  /* bottom */
  .photo-students { position: absolute; left: 0; top: 876px; width: 523px; height: 324px;
    background: linear-gradient(180deg, #f6f6f6 0%, #e6e4e6 55%, #c9c4c8 100%); }
  .info { position: absolute; left: 529px; top: 876px; width: 371px; height: 324px; background: var(--brown); color: var(--cream); padding: 26px 22px 0 18px; }
  .info-url { font-weight: 700; font-size: 14px; }
  .info-city { font-family: "Oswald", "Arial Narrow", sans-serif; font-weight: 400; font-size: 92px; line-height: 92px; letter-spacing: 2px; margin-top: -4px; }
  .notes { list-style: none; margin-top: 14px; }
  .notes li { position: relative; padding-left: 16px; font-style: italic; font-size: 13.5px; line-height: 17px; margin-bottom: 17px; }
  .notes li::before { content: ""; position: absolute; left: 2px; top: 5px; width: 6px; height: 6px; background: var(--cream); }
  .stripe { position: absolute; left: 523px; top: 876px; width: 6px; height: 324px; background: var(--white); }
</style>
</head>
<body>
<main class="flyer">

  <header class="brand">
    <span class="brand-dot"></span>
    <span class="brand-name">norvalia group</span>
  </header>

  <div class="rule-lime top"></div>
  <div class="photo-class" role="img" aria-label="Photo d'élèves souriants écrivant dans une salle de classe lumineuse"></div>

  <section class="address">
    <h2>TUNIS</h2>
    <p>Imm. les Palmiers, 2eme étage</p>
    <p>8 Rue du Lac Ontario</p>
    <p>(en face de l'Hotel Belvédère)</p>
    <p>1053 Les Rives du Lac 2</p>
    <div class="contact">
      <span class="contact-line phone">
        <svg viewBox="0 0 12 12"><path d="M2.5 1l2 2-1 1.3c.6 1.4 1.8 2.6 3.2 3.2L8 6.5l2 2-1.3 1.5C5 10 2 7 2 3.3z" fill="currentColor"/></svg>
        216 71 480 317
      </span>
      <span class="contact-line">
        <svg viewBox="0 0 12 12"><rect x="1" y="2.5" width="10" height="7" fill="none" stroke="currentColor"/><path d="M1 2.5l5 4 5-4" fill="none" stroke="currentColor"/></svg>
        tunis@norvalia.org
      </span>
      <span class="contact-line">
        <svg viewBox="0 0 12 12"><circle cx="6" cy="6" r="4.8" fill="none" stroke="currentColor"/><path d="M1.2 6h9.6M6 1.2c-2.4 3-2.4 6.6 0 9.6M6 1.2c2.4 3 2.4 6.6 0 9.6" fill="none" stroke="currentColor" stroke-width=".8"/></svg>
        www.norvalia.org
      </span>
    </div>
  </section>

  <div class="divider"></div>

  <section class="schedule">
    <div class="schedule-head"><h1>COURS D`ALLEMAND</h1></div>
    <div class="period">AVRIL<span class="sep"></span>MAI<span class="year">2016</span></div>

    <article class="session s1">
      <div class="session-title">Extensif Lundi/Mercredi/Vendredi<br>25/04/2016 - 20/05/2016</div>
      <div class="session-grid">
        <div class="slot left">18H30-21H30</div>
        <div class="slot"></div>
        <div class="groups left">A1.1 DK2136<br>A1.2 DK2137<br>A2.1 DK2138</div>
        <div class="groups center">A2.2 DK2139<br>B1.1 DK2140<br>B1.2 DK2141</div>
      </div>
    </article>

    <article class="session s2">
      <div class="session-title">Intensif Lundi - Vendredi<br>18/04/2016 - 06/05/2016</div>
      <div class="session-grid">
        <div class="slot center">09H30 - 12H30</div>
        <div class="slot center">13H00 - 16H00</div>
        <div class="groups mid">A1.1 DK2127<br>A1.2 DK2128<br>A2.1 DK2129<br>A2.2 DK2130<br>B1.1 DK2131</div>
        <div class="groups center right">A1.1 DK2132<br>B1.2 DK2133<br>B2.1 DK2134<br>B2.2 DK2135</div>
      </div>
    </article>

    <article class="session s3">
      <div class="session-title">Intensif Lundi - Vendredi<br>09/05/2016 - 27/05/2016</div>
      <div class="session-grid">
        <div class="slot center">09H30 - 12H30</div>
        <div class="slot center">13H00 - 16H00</div>
        <div class="groups mid">A1.1 DK2142<br>A1.2 DK2143<br>A2.1 DK2144<br>A2.2 DK2145<br>B1.1 DK2146<br>B1.2 DK2147</div>
        <div class="groups center right">A1.1 DK2148<br>A1.2 DK2149<br>B2.1 DK2150<br>B2.2 DK2151</div>
      </div>
    </article>
  </section>

  <div class="rule-lime bottom"></div>

  <div class="photo-students" role="img" aria-label="Photo d'un jeune étudiant souriant tenant des cahiers, avec un groupe d'étudiants debout derrière lui"></div>
  <div class="stripe"></div>

  <section class="info">
    <p class="info-url">www.facebook.com/norvalia</p>
    <p class="info-city">TUNIS</p>
    <ul class="notes">
      <li>Toute inscription doit im-perativement se faire au plus tard une semaine avant le debut des cours.</li>
      <li>Nombre minimum de 5 participants requis</li>
      <li>L'horaire des cours est susceptible d'être modifie. Prix par module 340 TND.</li>
    </ul>
  </section>

</main>
</body>
</html>
```